Basketball Training Facility Flyer Design

We need a killer flyer designed for our brand new state of the art basketball training facility here in Syracuse, Utah. This flyer will be distributed to coaches, parents and players in a large school district in Davis and Weber county, Utah. The purpose of the flyer is to announce the launch of the new facility and to encourage parents, coaches and players to come and try out the facility for a free initial session. We're offering a completely complimentary first training session to introduce customers to the facility at no cost.

We use technology and equipment that is typically found in PLQ-level training facilities and gymnasiums. Our website can be found here for some additional information - www.crestcourthoops.net. Customers can easily book and pay online through our website (the functionality will be done by the time we distribute the completed flyer).

The design needs to highlight the equipment we offer at the facility, because no other basketball training center has the same level of technology we do. We want the flyer to be clean and simple.

Please see must haves for specific details.

The size of the flyer we want to print is 5.75 inches by 9.5 inches.

Target Market(s)

Parents of basketball players of all skill levels age 8-18.

Industry/Entity Type

Training

Requirements
Must have
• Design must include this header: You want to dominate on the court. We have the formula to make that happen.

Design must include this sub header or highlight: Free Introductory Training Session!

The design must include our Logo

The design must include the photos attached of the Ravel, the Liftorra and the 37Twelve

Under the the photo of the Ravel 5200 (attached) please include this verbiage:
Game Shots in Game Spots at Game Speed

Under the photo of the Liftorra (see attached) please include this verbiage:
Improve Power, Agility and Speed like Never Before

Under the photo of the 37Twelve (attached) please include this verbiage:
Real Time Statistics to Improve Dribble Speed, Accuracy and Right / Left Comparison

Include this verbiage somewhere in the design: Technology Used by PLQ and the Best D-1 College Teams

The design must include a strong call to action: Call or Click Now to Schedule A Free Training Session!

The design must include our contact information in easy-to-read font and size (also specifically highlighting the website):

Schedule Online in Less Than 60 Seconds!
Call or Click
801-574-2918
www.crestcourthoops.net
Nice to have
• For examples of the type of design we like, please see the attached images labeled

Please use stock photos of your preference to go in the flyer (preferably images of youth basketball training or kids in basketball training)

We don't want the flyer to be too cluttered, so please use images at your discretion.

Thank you!

```html
<!DOCTYPE html>
<html lang="en">
<head>
<meta charset="utf-8">
<title>Crest Court Academy – Free Introductory Training Session</title>
<link rel="stylesheet" href="https://fonts.googleapis.com/css2?family=Arimo:ital,wght@0,400;0,700;1,700&family=Oswald:wght@700&display=swap">
<style>
  :root {
    --red: #e0211d;
    --ink: #1a1a1a;
    --white: #ffffff;
    --cream: #f4ead8;
    --grey-tab: #d6d6d6;
    --dominate: #8e8e8e;
    --floor-dark: #4a2208;
    --floor-mid: #b8621c;
    --floor-light: #e4983f;
    --frame: #2b1a10;
  }
  * { margin: 0; padding: 0; box-sizing: border-box; }
  html, body { width: 1200px; height: 726px; overflow: hidden; background: var(--frame); }
  .flyer {
    position: relative; width: 1200px; height: 726px; overflow: hidden;
    font-family: "Arimo", Arial, sans-serif;
    background: linear-gradient(180deg, #2a1a10 0%, #3a2414 60%, var(--floor-dark) 63%, var(--floor-mid) 78%, var(--floor-light) 90%, var(--floor-mid) 100%);
  }
  .hero-panel {
    position: absolute; left: 48px; top: 38px; width: 1130px; height: 420px;
    background: linear-gradient(90deg, #f3f3f3 0%, #ffffff 40%, #ffffff 75%, #ececec 100%);
  }
  .photo { position: absolute; }
  .photo-agility {
    left: 48px; top: 44px; width: 270px; height: 250px;
    background: radial-gradient(ellipse at 50% 45%, #3b3b3b 0%, #6a5a4c 45%, rgba(255,255,255,0) 72%);
  }
  .photo-dunk {
    left: 495px; top: 88px; width: 225px; height: 370px;
    background: radial-gradient(ellipse at 50% 50%, #7a3a22 0%, #a0302a 35%, rgba(255,255,255,0) 70%);
  }
  .photo-shooter {
    left: 900px; top: 195px; width: 278px; height: 263px;
    background: radial-gradient(ellipse at 45% 55%, #5b5b5b 0%, #b0794e 35%, rgba(255,255,255,0) 72%);
  }
  .promo-ribbon {
    position: absolute; left: 758px; top: 45px; width: 420px; height: 57px;
    background: linear-gradient(90deg, rgba(214,214,214,0) 0%, var(--grey-tab) 12%, #c8c8c8 100%);
    clip-path: polygon(6% 0, 100% 0, 100% 100%, 0 100%);
    text-align: right; padding: 6px 30px 0 0;
  }
  .promo-title { color: var(--red); font-weight: 700; font-style: italic; font-size: 20px; }
  .promo-sub { color: #555; font-size: 14px; margin-top: 2px; }
  .headline-lead, .headline-tail {
    position: absolute; color: var(--red); font-weight: 700; letter-spacing: 0.5px; line-height: 1;
  }
  .headline-lead { left: 322px; top: 78px; font-size: 32px; }
  .headline-tail { left: 762px; top: 152px; font-size: 30px; }
  .headline-main {
    position: absolute; left: 322px; top: 90px;
    font-family: "Oswald", Impact, sans-serif; font-size: 93px; line-height: 1;
    color: var(--dominate); letter-spacing: 4px;
  }
  .headline-main .reflection {
    display: block; transform: scaleY(-0.45); transform-origin: top;
    margin-top: 8px; opacity: 0.35; color: #b5b5b5;
  }
  .formula-band { position: absolute; left: 50px; top: 240px; width: 860px; height: 82px; }
  .formula-text {
    position: absolute; left: 172px; top: 262px;
    color: var(--white); font-weight: 700; font-size: 32px; line-height: 1.1;
    text-shadow: 0 2px 3px rgba(0,0,0,0.6);
  }
  .offer-tab {
    position: absolute; left: 48px; top: 318px; width: 240px; height: 30px;
    background: var(--grey-tab); border-radius: 0 15px 15px 0;
    color: var(--red); font-weight: 700; font-size: 20px; padding: 3px 0 0 12px;
  }
  .offer-list { position: absolute; left: 60px; top: 358px; list-style: none; font-weight: 700; font-size: 20px; line-height: 25px; }
  .offer-list .hot { color: var(--red); }
  .offer-list .plain { color: var(--ink); }
  .gear-card {
    position: absolute; top: 477px; height: 216px; background: var(--white);
    border: 2px solid #d8d8d8; box-shadow: 0 3px 8px rgba(0,0,0,0.45);
    text-align: center;
  }
  .gear-card p { font-size: 13px; line-height: 15px; color: var(--ink); }
  .gear-card .gear-photo { position: absolute; left: 8px; right: 8px; bottom: 8px; }
  .card-sensor { left: 48px; width: 260px; padding: 6px 22px; }
  .card-sensor .gear-photo { height: 118px; background: radial-gradient(ellipse at 40% 55%, #d0501c 0%, #a33c12 40%, #f4f4f4 70%); }
  .card-platform { left: 322px; width: 212px; padding: 6px 20px; }
  .card-platform .gear-photo { height: 158px; background: radial-gradient(ellipse at 50% 55%, #2f6fc4 0%, #9bb3cc 45%, #eeeeee 75%); }
  .card-rebounder { left: 550px; width: 160px; padding: 6px 28px; }
  .card-rebounder .gear-photo { height: 150px; background: radial-gradient(ellipse at 50% 55%, #c8302c 0%, #d9d9d9 50%, #f6f6f6 80%); }
  .cta {
    position: absolute; left: 730px; top: 484px; color: var(--cream);
    font-size: 20px; line-height: 23px; text-shadow: 0 1px 2px rgba(0,0,0,0.5);
  }
  .brand-mark { position: absolute; left: 1032px; top: 483px; width: 128px; height: 128px; }
  .brand-mark .dot {
    position: absolute; inset: 0; border-radius: 50%;
    background: var(--red); box-shadow: 0 3px 8px rgba(0,0,0,0.45);
  }
  .brand-mark .brand-name {
    position: absolute; left: 14px; top: 37px; width: 100px; text-align: center;
    color: var(--white); font-weight: 700; font-size: 15px; line-height: 18px;
  }
  .academy-name {
    position: absolute; left: 730px; top: 562px; color: var(--white);
    font-size: 29px; font-weight: 400; line-height: 1; white-space: nowrap;
    text-shadow: 0 2px 3px rgba(0,0,0,0.4);
  }
  .contact {
    position: absolute; left: 726px; top: 606px; width: 410px; text-align: center;
    color: var(--white); font-size: 20px; line-height: 26px; text-shadow: 0 1px 2px rgba(0,0,0,0.4);
  }
  .contact .web { font-weight: 700; font-size: 23px; color: var(--ink); text-shadow: none; margin-top: 2px; }
</style>
</head>
<body>
<main class="flyer">
  <div class="hero-panel"></div>

  <div class="photo photo-agility" role="img" aria-label="Athlete in a low agility stance among training cones"></div>
  <div class="photo photo-shooter" role="img" aria-label="Player lining up a jump shot with a basketball"></div>

  <div class="promo-ribbon">
    <div class="promo-title">Free Introductory Training Session!</div>
    <div class="promo-sub">Find out why Superior Technology = Superior Training</div>
  </div>

  <div class="headline-lead">YOU WANT TO</div>
  <h1 class="headline-main">DOMINATE<span class="reflection" aria-hidden="true">DOMINATE</span></h1>
  <div class="headline-tail">ON THE COURT ?</div>

  <svg class="formula-band" viewBox="0 0 860 82" aria-hidden="true">
    <defs>
      <linearGradient id="bandFade" x1="0" x2="1">
        <stop offset="0" stop-color="#9a9a9a" stop-opacity="0.2"/>
        <stop offset="0.35" stop-color="#8a8a8a"/>
        <stop offset="1" stop-color="#9a9a9a" stop-opacity="0.15"/>
      </linearGradient>
    </defs>
    <polygon points="0,0 820,0 860,41 820,82 0,82 40,41" fill="url(#bandFade)"/>
    <g fill="#ffffff" opacity="0.35">
      <polygon points="60,0 90,0 130,41 90,82 60,82 100,41"/>
      <polygon points="220,0 250,0 290,41 250,82 220,82 260,41"/>
      <polygon points="380,0 410,0 450,41 410,82 380,82 420,41"/>
      <polygon points="690,0 720,0 760,41 720,82 690,82 730,41"/>
    </g>
  </svg>
  <div class="photo photo-dunk" role="img" aria-label="Player rising for a one-handed dunk"></div>
  <p class="formula-text">We have the formula to make that happen</p>

  <div class="offer-tab">Our training offerings:</div>
  <ul class="offer-list">
    <li class="hot">One on one / Individual Sessions</li>
    <li class="plain">*Group Sessions (2-5 players with discounts applying)</li>
    <li class="hot">Team Training</li>
    <li class="hot">Monthly Memberships</li>
  </ul>

  <section class="gear-card card-sensor">
    <p>Basketball Sensors with Real Time Statistics to Improve Dribble Speed, Accuracy and Right / Left Comparison</p>
    <div class="gear-photo" role="img" aria-label="37Twelve sensor basketball beside a phone showing stats"></div>
  </section>
  <section class="gear-card card-platform">
    <p>Improve Power, Agility and Speed like Never Before</p>
    <div class="gear-photo" role="img" aria-label="Athlete training on the Liftorra resistance platform"></div>
  </section>
  <section class="gear-card card-rebounder">
    <p>Game Shots in Game Spots at Game Speed</p>
    <div class="gear-photo" role="img" aria-label="Ravel 5200 shooting machine with net"></div>
  </section>

  <p class="cta">Call or Click Now to Schedule<br>A Free Training Session!</p>

  <div class="brand-mark">
    <span class="dot"></span>
    <span class="brand-name">CREST COURT ACADEMY</span>
  </div>

  <h2 class="academy-name">Crest Court Academy</h2>
  <div class="contact">
    <p>Schedule Online in Less Than 60 Seconds!</p>
    <p>Call or Click: 801-574-2918</p>
    <p class="web">www.crestcourthoops.net</p>
  </div>
</main>
</body>
</html>
```